Marrowby's Vacation Rentals Business Card

Multi Million dollar villa rentals in the Dominican Republic.

Industry/Entity Type

Business

Contact Information for Business Card

I am looking for a high-end look around my company name/logo (see attached) on one side incorporating the following info: first and last name, title, address, phone #, email and company website. On the backside I want to add a full color picture of one of our villas (see attached).

```html
<!DOCTYPE html>
<html lang="en">
<head>
<meta charset="utf-8">
<title>Marrowby's Vacation Rentals – Business Card</title>
<link rel="stylesheet" href="https://fonts.googleapis.com/css2?family=Arimo:wght@400;700&display=swap">
<style>
  :root {
    --backdrop: #2b2b2b;
    --card-white: #f4f4f4;
    --ink: #111111;
    --muted: #6a6a6a;
    --accent: #d2552f;
    --sun: #f28a3a;
    --band: #0c0c0c;
    --contact: #e8e8e8;
    --sky: #7fb4e6;
    --villa: #e9e6df;
    --pool: #1f8fd6;
  }
  * { box-sizing: border-box; margin: 0; padding: 0; }
  html, body {
    width: 1200px; height: 997px; overflow: hidden;
    background: var(--backdrop);
    font-family: "Arimo", Arial, sans-serif;
  }
  .stage { position: relative; width: 1200px; height: 997px; }

  .card {
    position: absolute;
    width: 520px; height: 298px;
    box-shadow: 0 18px 40px rgba(0,0,0,.55);
    overflow: hidden;
  }

  /* Back side: villa photograph */
  .card--back { left: 90px; top: 130px; }
  .villa-photo {
    position: absolute; inset: 0;
    background: linear-gradient(180deg, var(--sky) 0%, #cfe2f2 28%, var(--villa) 45%, #d9d4c8 68%, var(--pool) 82%, #136fae 100%);
  }
  .back-brand {
    position: absolute; right: 26px; top: 150px;
    display: flex; align-items: center; gap: 8px;
  }
  .back-brand .brand-dot { width: 18px; height: 18px; }
  .back-brand .brand-name { font-size: 15px; }

  /* Front side */
  .card--front { left: 590px; top: 450px; background: var(--card-white); }
  .card-waves { position: absolute; inset: 0; }

  .brand {
    position: absolute; left: 42px; top: 58px;
    display: flex; align-items: center; gap: 12px;
  }
  .brand-dot {
    width: 36px; height: 36px; border-radius: 50%;
    background: var(--sun); flex: none;
  }
  .brand-name {
    font-weight: 700; font-size: 25px; color: var(--ink);
    white-space: nowrap;
  }

  .holder {
    position: absolute; right: 40px; top: 106px; text-align: right;
  }
  .holder-name { font-weight: 700; font-size: 15px; color: var(--ink); letter-spacing: .3px; }
  .holder-title { font-size: 12px; color: var(--muted); margin-top: 2px; }

  .contact {
    position: absolute; left: 22px; top: 218px;
    list-style: none;
  }
  .contact li {
    display: flex; align-items: center; gap: 8px;
    font-size: 13px; line-height: 17px; color: var(--contact);
  }
  .contact svg { width: 10px; height: 10px; flex: none; fill: var(--accent); }
  .contact .web {
    color: var(--accent); font-weight: 700; letter-spacing: 2.5px; padding-left: 18px;
  }
</style>
</head>
<body>
<main class="stage">

  <section class="card card--back" aria-label="Card back">
    <div class="villa-photo" role="img" aria-label="Photograph of a white two-storey villa with arched terraces, palm trees and blue loungers beside a swimming pool"></div>
    <div class="back-brand">
      <span class="brand-dot"></span>
      <span class="brand-name">Marrowby's Vacation Rentals</span>
    </div>
  </section>

  <section class="card card--front" aria-label="Card front">
    <svg class="card-waves" viewBox="0 0 520 298" preserveAspectRatio="none" aria-hidden="true">
      <path d="M0 204 C170 160 360 218 520 172 L520 298 L0 298 Z" fill="var(--band)"/>
      <path d="M0 192 C170 148 360 206 520 160" fill="none" stroke="var(--accent)" stroke-width="6"/>
    </svg>

    <div class="brand">
      <span class="brand-dot"></span>
      <span class="brand-name">Marrowby's Vacation Rentals</span>
    </div>

    <div class="holder">
      <p class="holder-name">DARA WHITFIELD</p>
      <p class="holder-title">Managing Director</p>
    </div>

    <ul class="contact">
      <li>
        <svg viewBox="0 0 10 10"><path d="M2 0 L4 2.5 L3 3.5 Q4.5 6 6.5 7 L7.5 6 L10 8 L8.5 10 Q3 9.5 0 1.5 Z"/></svg>
        1300 418 522
      </li>
      <li>
        <svg viewBox="0 0 10 10"><path d="M0 2 H10 V8 H0 Z M0 2 L5 5.5 L10 2" /></svg>
        dara.whitfield@marrowbys.com
      </li>
      <li>
        <svg viewBox="0 0 10 10"><path d="M5 0 A3.5 3.5 0 0 1 8.5 3.5 Q8.5 6 5 10 Q1.5 6 1.5 3.5 A3.5 3.5 0 0 1 5 0 Z"/></svg>
        58 Harbour Lane, Sydney 2000
      </li>
      <li class="web">www.marrowbys.com</li>
    </ul>
  </section>

</main>
</body>
</html>
```